Crypto currency project website revamp

Our current website is: http://www.galvoranet.org

The new logo is also attached.

Here are some examples of the other crypto websites. Our goal is to re-make the above website to look and feel like the followings:

1) https://quendalabs.com/

2) https://vorti.io/

3) https://plimset.network/#/

Please submit your designs. Once we found the right design we need to interate a bit and add 3 or 4 more sections to it.

The coded website needs to be responsive

```html
<!DOCTYPE html>
<html lang="en">
<head>
<meta charset="utf-8">
<title>Galvora Network</title>
<link href="https://fonts.googleapis.com/css2?family=Montserrat:wght@500;600;700&family=Raleway:wght@400;500;600&display=swap" rel="stylesheet">
<style>
:root{
  --ink:#111418;
  --body:#4a4f57;
  --white:#ffffff;
  --blue:#4a74f0;
  --sky:#4cb5e2;
  --mint:#6ff0c8;
  --aqua:#58d8d3;
  --black:#000000;
  --muted:#9aa0a8;
  --line:#e3e6ea;
}
*{box-sizing:border-box;margin:0;padding:0}
html,body{width:1200px;height:4147px;overflow:hidden}
body{position:relative;background:var(--white);font-family:"Raleway",sans-serif;color:var(--body)}
.abs{position:absolute}
h1,h2,h3{font-family:"Montserrat",sans-serif;color:var(--ink)}

/* hero */
.hero{left:0;top:0;width:1200px;height:660px;
  background:radial-gradient(ellipse at 60% 40%,#1d3a5a 0%,#0d1a2c 45%,#05080f 100%);
  clip-path:polygon(0 0,100% 0,100% 525px,0 660px)}
.nav-brand{left:100px;top:36px;color:var(--white);font-family:"Montserrat",sans-serif;font-weight:700;font-size:17px}
.nav{right:100px;top:36px;display:flex;gap:34px}
.nav a{color:var(--white);text-decoration:none;font-size:16px;font-weight:500}
.hero-title{left:0;width:1200px;top:215px;text-align:center;color:var(--white);font-size:70px;font-weight:600}
.hero-sub{left:0;width:1200px;top:302px;text-align:center;color:#e8ecf4;font-size:32px;font-weight:400}
.btn{display:inline-block;border-radius:24px;background:linear-gradient(90deg,var(--blue),var(--mint));color:var(--white);font-weight:500;text-align:center}
.hero-btn{left:486px;top:378px;width:230px;height:44px;line-height:44px;font-size:17px}
.arrow{top:312px;width:24px;height:40px}

/* intro */
.sec-title{left:0;width:1200px;text-align:center;font-size:36px;font-weight:600}
.rule{left:510px;width:180px;height:4px;background:linear-gradient(90deg,var(--blue),var(--mint))}
.intro-text{left:210px;width:780px;top:868px;text-align:center;font-size:14px;line-height:25px}
.feature{top:965px;width:230px;text-align:center;font-size:15px;line-height:25px}
.feature svg{display:block;margin:0 auto 20px}

/* intro band */
.band{left:0;top:1230px;width:1200px;height:600px;
  background:linear-gradient(110deg,var(--blue) 0%,#4a8fe8 50%,var(--sky) 100%);
  clip-path:polygon(0 130px,100% 0,100% 462px,0 600px)}
.band-art{left:760px;top:1230px;width:440px;height:600px;
  background:linear-gradient(160deg,rgba(120,220,240,.35),rgba(255,255,255,0));
  clip-path:polygon(0 118px,100% 0,100% 462px,0 582px)}
.band-title{left:100px;top:1438px;color:var(--white);font-size:36px;font-weight:600}
.band-text{left:100px;top:1500px;width:700px;color:#eef3ff;font-size:14px;line-height:27px}
.band-btn{left:100px;top:1656px;width:144px;height:40px;line-height:40px;font-size:15px}

/* comparison */
.illus{border-radius:16px}
.checks{list-style:none;font-size:22px;color:var(--ink);line-height:40px}
.checks li{display:flex;align-items:center;gap:16px}

/* team */
.team{left:0;top:2571px;width:1200px;height:720px;
  background:linear-gradient(180deg,var(--blue) 0%,#4c9ee2 45%,var(--aqua) 100%);
  clip-path:polygon(0 139px,100% 0,100% 575px,0 720px)}
.team-title{left:0;width:1200px;top:2752px;text-align:center;color:var(--white);font-size:36px;font-weight:600}
.card{top:2840px;width:455px;height:174px;background:linear-gradient(135deg,var(--white) 60%,#b9f5e5 60%);display:flex;box-shadow:0 6px 18px rgba(0,0,0,.12)}
.card .photo{width:174px;height:174px;background:linear-gradient(160deg,#6b5a4c,#2c2a2a)}
.card .info{padding:28px 22px 0 40px;flex:1;position:relative}
.card h3{font-size:22px;font-weight:600;margin-bottom:12px}
.card p{font-size:14px;line-height:20px}
.card .social{position:absolute;right:18px;bottom:14px;display:flex;gap:8px}
.card .social span{width:10px;height:10px;border-radius:50%;background:var(--blue)}
.dots{left:578px;top:3086px;display:flex;gap:8px}
.dots span{width:9px;height:9px;border-radius:50%;background:var(--white)}
.dots span:first-child{background:var(--mint)}

/* partners */
.partner{top:3404px;width:140px;height:110px;border:1px solid var(--line);border-radius:4px;box-shadow:0 2px 6px rgba(0,0,0,.08);display:flex;align-items:center;justify-content:center;font-size:18px;font-weight:600;color:#2a2d33}

/* footer */
.footer{left:0;top:3622px;width:1200px;height:525px;background:var(--black);clip-path:polygon(0 138px,100% 0,100% 100%,0 100%)}
.f-head{color:#d0d4da;font-size:18px;font-weight:500}
.f-small{color:#bfc3c9;font-size:12px}
.f-links{list-style:none;font-size:13px;line-height:25px;color:#bfc3c9}
.sub{left:100px;top:3902px;width:265px;height:36px;border-radius:18px;background:var(--white);display:flex;align-items:center;justify-content:space-between;padding-left:16px;font-size:12px;color:var(--muted)}
.sub span{height:30px;line-height:30px;padding:0 14px;margin-right:3px;border-radius:15px;background:var(--mint);color:var(--ink);font-weight:600}
.f-social{left:100px;top:3990px;display:flex;gap:20px}
.f-social span{width:12px;height:12px;border-radius:50%;background:#d0d4da}
</style>
</head>
<body>

<section class="abs hero" role="img" aria-label="Dark starfield with glowing network lines"></section>
<div class="abs nav-brand">Galvora Network</div>
<nav class="abs nav"><a href="#">Home</a><a href="#">What Is Galvora</a><a href="#">Codeyard</a><a href="#">Yellow Paper</a><a href="#">Contact</a></nav>
<svg class="abs arrow" style="left:38px" viewBox="0 0 24 40"><path d="M18 4 6 20l12 16" fill="none" stroke="#fff" stroke-width="4"/></svg>
<svg class="abs arrow" style="right:38px" viewBox="0 0 24 40"><path d="M6 4l12 16L6 36" fill="none" stroke="#fff" stroke-width="4"/></svg>
<h1 class="abs hero-title">Galvora Network</h1>
<p class="abs hero-sub">Future of cryptocurrencies we were promised</p>
<a class="abs btn hero-btn">Request A Quote</a>

<h2 class="abs sec-title" style="top:766px">What is the Plimset Network?</h2>
<div class="abs rule" style="top:828px"></div>
<p class="abs intro-text">Sed ut perspiciatis unde omnis iste natus error sit voluptatem accusantium doloremque laudantium, totam rem aperiam, eaque ipsa quae ab illo inventore veritatis et quasi architecto beatae vitae dicta sunt explicabo.</p>

<div class="abs feature" style="left:81px"><svg width="46" height="46" viewBox="0 0 46 46"><path d="M23 4 38 10v12c0 10-7 17-15 20C15 39 8 32 8 22V10z" fill="none" stroke="#4a74f0" stroke-width="2"/><path d="M23 15l3 6 6 1-4 4 1 6-6-3-6 3 1-6-4-4 6-1z" fill="none" stroke="#58d8d3" stroke-width="2"/></svg>Lorem ipsum dolor sit amet, consectetur adipiscing elit, sed do eiusmod.</div>
<div class="abs feature" style="left:350px"><svg width="46" height="46" viewBox="0 0 46 46"><path d="M4 10h16c2 0 3 1 3 3v25c0-2-1-3-3-3H4zM42 10H26c-2 0-3 1-3 3v25c0-2 1-3 3-3h16z" fill="none" stroke="#4a74f0" stroke-width="2"/><path d="M9 18h9M9 24h9M28 18h9M28 24h9" stroke="#58d8d3" stroke-width="2"/></svg>Lorem ipsum dolor sit amet, consectetur adipiscing elit, sed do eiusmod.</div>
<div class="abs feature" style="left:618px"><svg width="46" height="46" viewBox="0 0 46 46"><circle cx="23" cy="23" r="18" fill="none" stroke="#4a74f0" stroke-width="2"/><path d="M5 23h36M23 5c-7 8-7 28 0 36M23 5c7 8 7 28 0 36" fill="none" stroke="#58d8d3" stroke-width="2"/></svg>Lorem ipsum dolor sit amet, consectetur adipiscing elit, sed do eiusmod.</div>
<div class="abs feature" style="left:886px"><svg width="46" height="46" viewBox="0 0 46 46"><path d="M23 4c6 5 8 13 6 24H17C15 17 17 9 23 4z" fill="none" stroke="#4a74f0" stroke-width="2"/><path d="M17 28l-5 8h7M29 28l5 8h-7M20 38h6" fill="none" stroke="#58d8d3" stroke-width="2"/><circle cx="23" cy="16" r="3" fill="none" stroke="#58d8d3" stroke-width="2"/></svg>Lorem ipsum dolor sit amet, consectetur adipiscing elit, sed do eiusmod.</div>

<section class="abs band"></section>
<div class="abs band-art" role="img" aria-label="Faint globe made of connected network nodes"></div>
<h2 class="abs band-title">What Is Galvora?</h2>
<p class="abs band-text">Galvora is a peer-to-peer graph to exchange and transact most crypto-currencies with NO fee or counterparty risk. Galvora is a decentralized, and distributed ledger technology with built-in support to read across chains. This means Galvora is able to represent almost any crypto-currency and allow them to be exchanged and transacted in the Galvora network. Kobalcoin is expensive and slow to trade. In Galvora network Kobalcoin can be traded or exchanged fast, and without any fees.</p>
<a class="abs btn band-btn">Read More</a>

<h2 class="abs sec-title" style="top:1935px">Centralized versus Decentralized</h2>
<div class="abs rule" style="top:1996px"></div>
<div class="abs illus" style="left:166px;top:2032px;width:290px;height:208px;background:linear-gradient(135deg,#dfe9fb,#7fb0ee 55%,#57d6b6)" role="img" aria-label="Isometric servers guarded by a shield and connected laptops"></div>
<ul class="abs checks" style="left:672px;top:2086px">
  <li><svg width="16" height="14" viewBox="0 0 16 14"><path d="M2 7l4 4 8-9" fill="none" stroke="#4a74f0" stroke-width="3"/></svg>Exchange controls the funds</li>
  <li><svg width="16" height="14" viewBox="0 0 16 14"><path d="M2 7l4 4 8-9" fill="none" stroke="#4a74f0" stroke-width="3"/></svg>Tooling limited by exchange</li>
  <li><svg width="16" height="14" viewBox="0 0 16 14"><path d="M2 7l4 4 8-9" fill="none" stroke="#4a74f0" stroke-width="3"/></svg>Prone to hack</li>
</ul>
<ul class="abs checks" style="left:221px;top:2302px">
  <li><svg width="16" height="14" viewBox="0 0 16 14"><path d="M2 7l4 4 8-9" fill="none" stroke="#4a74f0" stroke-width="3"/></svg>Only user controls the funds</li>
  <li><svg width="16" height="14" viewBox="0 0 16 14"><path d="M2 7l4 4 8-9" fill="none" stroke="#4a74f0" stroke-width="3"/></svg>Open community tooling</li>
  <li><svg width="16" height="14" viewBox="0 0 16 14"><path d="M2 7l4 4 8-9" fill="none" stroke="#4a74f0" stroke-width="3"/></svg>Can NOT be hacked</li>
</ul>
<div class="abs illus" style="left:724px;top:2262px;width:258px;height:199px;background:radial-gradient(circle,#5b87b8,#c8d8e6 70%,#ffffff)" role="img" aria-label="Distributed servers linked around a central hub"></div>

<section class="abs team"></section>
<h2 class="abs team-title">Meet The Team</h2>
<article class="abs card" style="left:100px">
  <div class="photo" role="img" aria-label="Portrait photo of team member"></div>
  <div class="info"><h3>Mara Velden</h3><p>Sed ut perspiciatis unde omnis iste atus error sit voluptatem accusantium</p><div class="social"><span></span><span></span><span></span></div></div>
</article>
<article class="abs card" style="left:644px">
  <div class="photo" role="img" aria-label="Portrait photo of team member"></div>
  <div class="info"><h3>Tobin Reyes</h3><p>Sed ut perspiciatis unde omnis iste atus error sit voluptatem accusantium</p><div class="social"><span></span><span></span><span></span></div></div>
</article>
<div class="abs dots"><span></span><span></span><span></span></div>

<div class="abs partner" style="left:100px">Corvane</div>
<div class="abs partner" style="left:271px">Sendvale</div>
<div class="abs partner" style="left:442px">Brightlot</div>
<div class="abs partner" style="left:614px">Oakform</div>
<div class="abs partner" style="left:785px">Mercato</div>
<div class="abs partner" style="left:957px">Primeloft</div>

<footer class="abs footer"></footer>
<div class="abs f-head" style="left:100px;top:3820px">Newsletter</div>
<div class="abs f-small" style="left:100px;top:3866px">Get Offers &amp; update from Galvora</div>
<div class="abs sub">Email Address<span>SUBSCRIBE</span></div>
<div class="abs f-social"><span></span><span></span><span></span><span></span><span></span></div>
<div class="abs f-head" style="left:719px;top:3820px">Importants</div>
<ul class="abs f-links" style="left:719px;top:3860px"><li>Home</li><li>What is Galvora</li><li>Codeyard</li><li>Yellow Paper</li><li>Contact</li></ul>
<div class="abs f-head" style="left:907px;top:3820px">Other</div>
<ul class="abs f-links" style="left:907px;top:3860px"><li>Privacy Policy</li><li>Faq</li><li>Terms &amp; Conditions</li></ul>
<div class="abs f-small" style="right:100px;top:4085px">© 2018 Copyrights Galvora network All Rights Reserved</div>

</body>
</html>
```